Website for the Mendwell Kiosk (sm): A mobile station with first aid supplies, staffed by our medics!

Hi! We need to create a new website. Will also need to be able to control the back-end - we need to be able to control and change the site easily, perhaps with css? This will be an offering from our company, Lanternfield Consulting LLC. We want this site to reflect the service: a mobile Mendwell Kiosk, staffed with our medics (see attached photo) - we will be hired to work at parties, children's birthday parties, sporting events, road races and triathlons, weddings, etc. We want companies, corporations and event planners to hire us! We will need 4 or 5 tabs/links to illustrate our offerings. We like warm colors and brightness - light and inviting, to attract attention. As you see, our company logo is blue - but the front panel illustration is a velum insert and may be changed to any theme. The final design should communicate that you should never plan an event without one of our Mendwell Kiosks! We want the site to be inviting, like some of these referenced below:

OUR FAVORITE (Especially if the bottles on the home page were actually links) willow-demo.tilecrate.com

Others we like:

https://www.tilecrate.com/templates/food-drink

meadow-demo.tilecrate.com

https://www.kinroost.com/

https://www.zippazzaa.com/

https://www.badgersbiscotti.com/

Event Planners, Wedding Coordinators, Large corporations, Sports Event Managers, Fun Run/Triathlon Coordinators, Parents, Health and Safety Managers

• Calibri

• Warm, inviting colors, 4 or 5 tabs/links, our logo, easy to navigate, the ability to be easily altered, room for photos.
• Must be able to link to our other company website: www.lanternfieldconsultingllc.com
• Boring fonts, darkness, difficulty with naviation

```html
<!DOCTYPE html>
<html lang="en">
<head>
<meta charset="utf-8">
<title>Mendwell Kiosk</title>
<link href="https://fonts.googleapis.com/css2?family=Montserrat:wght@600;700;800&family=Open+Sans:wght@400;600;700&display=swap" rel="stylesheet">
<style>
:root{
  --orange:#f08a1c;
  --orange-deep:#e0761a;
  --navy:#1f3a52;
  --navy-deep:#17293b;
  --beige:#ece6d8;
  --beige-shadow:#e2ddd2;
  --ink:#151515;
  --body-ink:#333;
  --white:#fff;
  --pink:#ec2d7a;
  --yellow:#f5d10f;
  --green:#2ec05a;
  --blue-btn:#5b7fd6;
  --cyan:#1fb3e8;
  --cta-orange:#f5870f;
}
*{box-sizing:border-box;margin:0;padding:0}
html,body{width:1200px;height:4245px;overflow:hidden}
body{position:relative;background:var(--beige);font-family:'Open Sans',sans-serif;color:var(--body-ink)}
.abs{position:absolute}
.band{position:absolute;left:0;width:1200px;overflow:hidden}
.band-photo{position:absolute;inset:0}
h1,h2,.btn,.nav-label{font-family:'Montserrat',sans-serif}
.btn{position:absolute;display:flex;align-items:center;justify-content:center;font-size:13px;font-weight:700;color:var(--white);text-transform:uppercase;letter-spacing:.5px}
.section-title{position:absolute;font-size:40px;font-weight:800;text-transform:uppercase;line-height:1.18;letter-spacing:.5px}
.section-copy{position:absolute;font-size:19px;line-height:1.7}
.photo{position:absolute;box-shadow:0 10px 24px rgba(0,0,0,.28)}
.photo-backer{position:absolute;background:var(--beige-shadow)}
.on-dark{color:var(--white)}

/* hero */
.hero{top:0;height:586px}
.hero-photo{background:linear-gradient(180deg,#3d4650 0%,#5d6a5a 45%,#4f7a3c 75%,#3e6a2e 100%)}
.hero-shade{position:absolute;inset:0;background:rgba(20,30,40,.28)}
.logo-box{position:absolute;left:93px;top:0;width:218px;height:175px;background:var(--white);clip-path:polygon(18% 0,100% 0,82% 100%,0 100%);display:flex;flex-direction:column;align-items:center;justify-content:center;gap:8px}
.logo-dot{width:38px;height:38px;border-radius:50%;background:#1a3c8f}
.logo-name{font-family:'Open Sans',sans-serif;font-size:20px;font-weight:600;color:#1a3c8f}
.nav{position:absolute;top:28px;left:480px;display:flex}
.nav-item{width:108px;display:flex;flex-direction:column;align-items:center;gap:12px}
.nav-item svg{width:30px;height:30px}
.nav-label{font-size:11px;font-weight:700;color:var(--white);letter-spacing:.3px}
.nav-item.active::after{content:"";width:42px;height:3px;background:var(--yellow);margin-top:-4px}
.hero-title{position:absolute;top:282px;left:0;width:1200px;text-align:center;font-size:40px;font-weight:800;color:var(--white);line-height:1.25;text-transform:uppercase}
.hero-dots{position:absolute;top:552px;left:565px;display:flex;gap:10px}
.hero-dots span{width:8px;height:8px;border-radius:50%;background:rgba(255,255,255,.6)}
.hero-dots span:first-child{background:var(--white)}

/* bands */
.orange-photo{background:linear-gradient(120deg,#ef8b22,#f59a34 45%,#e57a1a)}
.navy-photo{background:linear-gradient(120deg,#243d55,#2f4c66 50%,#1d3348)}
.footer-photo{background:linear-gradient(120deg,#2a4158,#34506a 50%,#22384e)}

.subscribe{position:absolute;left:192px;top:3953px;width:815px;height:63px;background:var(--white);display:flex;align-items:center}
.subscribe-field{flex:1;padding-left:34px;font-size:15px;color:#999}
.subscribe .btn{position:static;width:178px;height:53px;margin-right:5px;background:var(--cta-orange);font-size:14px}

.bottom-bar{top:4118px;height:127px;background:var(--beige)}
.social{position:absolute;left:107px;top:52px;display:flex;gap:10px}
.social span{width:26px;height:26px;border-radius:50%;background:var(--orange-deep)}
.copyright{position:absolute;left:362px;top:58px;font-size:12px;color:#444}
.brand-mark{position:absolute;left:880px;top:42px;display:flex;align-items:center;gap:10px}
.brand-mark .dot{width:22px;height:22px;border-radius:50%;background:#2b6ea8}
.brand-mark .name{font-size:19px;font-weight:600;color:#1f3550}
</style>
</head>
<body>

<header class="band hero">
  <div class="band-photo hero-photo" role="img" aria-label="Medic kneeling beside an injured football player on a stadium pitch"></div>
  <div class="hero-shade"></div>
  <div class="logo-box">
    <span class="logo-dot"></span>
    <span class="logo-name">Mendwell Kiosk</span>
  </div>
  <nav class="nav">
    <div class="nav-item active"><svg viewBox="0 0 30 30" fill="none" stroke="#fff" stroke-width="2"><path d="M5 14 15 5l10 9M8 12v13h14V12"/></svg><span class="nav-label">HOME</span></div>
    <div class="nav-item"><svg viewBox="0 0 30 30" fill="none" stroke="#fff" stroke-width="2"><rect x="7" y="4" width="16" height="22" rx="2"/><circle cx="15" cy="12" r="3"/><path d="M10 21h10"/></svg><span class="nav-label">ABOUT US</span></div>
    <div class="nav-item"><svg viewBox="0 0 30 30" fill="none" stroke="#fff" stroke-width="2"><rect x="4" y="6" width="22" height="18" rx="2"/><path d="M8 19l5-5 4 3 5-6"/></svg><span class="nav-label">SERVICES</span></div>
    <div class="nav-item"><svg viewBox="0 0 30 30" fill="none" stroke="#fff" stroke-width="2"><path d="M5 6h20v13H13l-5 5v-5H5z"/></svg><span class="nav-label">TESTIMONIALS</span></div>
    <div class="nav-item"><svg viewBox="0 0 30 30" fill="none" stroke="#fff" stroke-width="2"><circle cx="15" cy="15" r="11"/><path d="M12 12a3 3 0 1 1 4 3v2M15 21v1"/></svg><span class="nav-label">FAQ'S</span></div>
    <div class="nav-item"><svg viewBox="0 0 30 30" fill="none" stroke="#fff" stroke-width="2"><path d="M8 4l4 5-3 3a14 14 0 0 0 9 9l3-3 5 4-3 4C13 26 4 17 4 7z"/></svg><span class="nav-label">CONTACT US</span></div>
  </nav>
  <h1 class="hero-title">We are a mobile Mendwell Kiosk,<br>staffed with our medics</h1>
  <div class="btn" style="left:490px;top:416px;width:218px;height:48px;background:var(--pink)">Hire us</div>
  <div class="hero-dots"><span></span><span></span><span></span><span></span></div>
</header>

<section class="band" style="top:586px;height:555px">
  <div class="band-photo orange-photo" role="img" aria-label="Party crowd tinted in warm orange"></div>
  <h2 class="section-title on-dark" style="left:107px;top:136px">Work at parties</h2>
  <p class="section-copy on-dark" style="left:107px;top:222px;width:460px">Sed ut perspiciatis unde omnis iste natus error sit voluptatem accusantium doloremque laudantium, totam rem aperiam, eaque</p>
  <div class="btn" style="left:107px;top:359px;width:221px;height:54px;background:var(--yellow)">Read more</div>
  <div class="photo" style="left:614px;top:99px;width:495px;height:368px;background:linear-gradient(160deg,#8fc4d8,#d8c24a 55%,#6a6a6a)" role="img" aria-label="Ambulance with open rear doors and a paramedic"></div>
</section>

<section class="band" style="top:1141px;height:704px;background:var(--beige)">
  <div class="photo-backer" style="left:161px;top:169px;width:501px;height:436px"></div>
  <div class="photo" style="left:107px;top:104px;width:507px;height:439px;background:linear-gradient(150deg,#c9b9a8,#8aa6c4 55%,#d9d2c4)" role="img" aria-label="Parent bandaging a child's arm"></div>
  <h2 class="section-title" style="left:719px;top:104px;color:var(--ink)">Children's<br>birthday<br>parties</h2>
  <p class="section-copy" style="left:719px;top:275px;width:360px">Sed ut perspiciatis unde omnis iste natus error sit voluptatem accusantium doloremque laudantium, totam rem aperiam, eaque ipsa quae ab illo inventore veritatis</p>
  <div class="btn" style="left:719px;top:503px;width:218px;height:54px;background:var(--green)">Read more</div>
</section>

<section class="band" style="top:1845px;height:555px">
  <div class="band-photo navy-photo" role="img" aria-label="Runners on a track tinted in dark blue"></div>
  <h2 class="section-title on-dark" style="left:105px;top:150px">Sporting events</h2>
  <p class="section-copy on-dark" style="left:105px;top:245px;width:470px">Sed ut perspiciatis unde omnis iste natus error sit voluptatem accusantium doloremque laudantium, totam rem aperiam, eaque</p>
  <div class="btn" style="left:105px;top:379px;width:220px;height:54px;background:var(--orange-deep)">Read more</div>
  <div class="photo" style="left:614px;top:96px;width:495px;height:365px;background:linear-gradient(160deg,#9a9a9a,#c4c4c4 50%,#8a8a8a)" role="img" aria-label="Medic treating a seated runner beside a first aid kit"></div>
</section>

<section class="band" style="top:2400px;height:699px;background:var(--beige)">
  <div class="photo-backer" style="left:161px;top:167px;width:501px;height:436px"></div>
  <div class="photo" style="left:107px;top:99px;width:504px;height:439px;background:linear-gradient(150deg,#e6ebef,#5b8fc9 50%,#b8a38a)" role="img" aria-label="Medics caring for an athlete on a stretcher under a tent"></div>
  <h2 class="section-title" style="left:719px;top:141px;color:var(--ink)">Road races &amp;<br>triathlons</h2>
  <p class="section-copy" style="left:719px;top:285px;width:360px">Sed ut perspiciatis unde omnis iste natus error sit voluptatem accusantium doloremque laudantium, totam rem aperiam, eaque ipsa quae ab illo inventore veritatis</p>
  <div class="btn" style="left:719px;top:500px;width:218px;height:52px;background:var(--blue-btn)">Read more</div>
</section>

<section class="band" style="top:3099px;height:552px">
  <div class="band-photo orange-photo" role="img" aria-label="Wedding celebration tinted in warm orange"></div>
  <h2 class="section-title on-dark" style="left:107px;top:142px">Weddings</h2>
  <p class="section-copy on-dark" style="left:107px;top:250px;width:460px">Sed ut perspiciatis unde omnis iste natus error sit voluptatem accusantium doloremque laudantium, totam rem aperiam, eaque</p>
  <div class="btn" style="left:107px;top:382px;width:218px;height:51px;background:var(--cyan)">Read more</div>
  <div class="photo" style="left:614px;top:110px;width:495px;height:365px;background:linear-gradient(160deg,#8a3a30,#c8c2c0 50%,#2a3440)" role="img" aria-label="Paramedics attending to a patient"></div>
</section>

<section class="band" style="top:3651px;height:467px">
  <div class="band-photo footer-photo" role="img" aria-label="Medic standing beside an ambulance tinted in dark blue"></div>
  <h2 class="abs" style="left:0;top:130px;width:1200px;text-align:center;font-size:40px;font-weight:700;color:var(--white);text-transform:uppercase;letter-spacing:1px">Mendwell Kiosk</h2>
  <p class="abs on-dark" style="left:220px;top:212px;width:760px;text-align:center;font-size:12px;line-height:1.8">Book our mobile kiosk and trained medics for your next event. We bring supplies, care and calm so guests stay safe while you enjoy the day, from small parties to big races.</p>
</section>
<div class="subscribe">
  <span class="subscribe-field">example@mail.com</span>
  <div class="btn">Hire us</div>
</div>

<footer class="band bottom-bar">
  <div class="social"><span></span><span></span><span></span><span></span><span></span><span></span></div>
  <p class="copyright">© 2017 COMPANY NAME | ALL RIGHTS RESERVED</p>
  <div class="brand-mark"><span class="dot"></span><span class="name">Lanternfield Consulting</span></div>
</footer>

</body>
</html>
```